CREATE A BUSINESS CARD FOR A BOAT CLEANING SERVICE

WE ARE STARTING A NEW BOAT CLEANING BUSINESS. WE DIVE UNDERWATER TO CLEAN BOAT HULLS, JETTIES, UNDERWATER STRUCTURES ETC. WE ARE LOOKING FOR AN UPPERMARKET MODERN LOGO AND BUSINESS CARD AS ALOT OF OUR TARGET MARKET WILL BE HIGH END. YOU HAVE TO DESIGN A BUSINESS CARD AND LOGO SEPERATELY .
THE BUSINESS CARD DIMESNION MUST BE STANDARD SIZE.
The standard dimensions of a printed business card are 3.5 x 2 inches

Target Market(s)

UNDERWATER SERVICED

Industry/Entity Type

Business

Contact Information for Business Card

HALDANE SUBSEA SERVICES

Font styles to use
Serif

Colors

Designer to choose colors to be used in the design.

Requirements
Must have
• HALDANE
Nice to have
• dark
Should not have
• more than 3 colors

```html
<!DOCTYPE html>
<html lang="en">
<head>
<meta charset="utf-8">
<title>Haldane Subsea Services – Business Cards</title>
<link rel="stylesheet" href="https://fonts.googleapis.com/css2?family=Michroma&family=Roboto:wght@400&display=swap">
<style>
  :root {
    --page: #121216;
    --navy-deep: #12133a;
    --navy: #1f2160;
    --cyan: #0bb4ee;
    --periwinkle: #5258ab;
    --white: #f4f5fb;
  }
  html, body {
    margin: 0;
    width: 1200px;
    height: 900px;
    overflow: hidden;
    background: var(--page);
  }
  .canvas {
    position: relative;
    width: 1200px;
    height: 900px;
  }
  .card {
    position: absolute;
    width: 640px;
    height: 366px;
    background: linear-gradient(135deg, var(--navy-deep) 0%, var(--navy) 100%);
    overflow: hidden;
    box-shadow: 0 10px 30px rgba(0,0,0,0.5);
  }
  .card--back { left: 500px; top: 60px; background: linear-gradient(135deg, #18194a 0%, var(--navy) 100%); }
  .card--front { left: 60px; top: 474px; }

  .wordmark {
    font-family: "Michroma", sans-serif;
    color: var(--periwinkle);
    letter-spacing: 0.08em;
    line-height: 1.35;
    text-align: center;
  }
  .card--back .wordmark {
    position: absolute;
    left: 0; right: 0; top: 128px;
    font-size: 30px;
  }
  .card--back .wordmark .wordmark__sub { font-size: 19px; }

  .card--front .wordmark {
    position: absolute;
    left: 320px; width: 290px; top: 180px;
    font-size: 21px;
  }
  .card--front .wordmark .wordmark__sub { font-size: 13px; }

  .holder {
    position: absolute;
    left: 40px; top: 36px;
  }
  .holder__name {
    font-family: "Michroma", sans-serif;
    font-size: 20px;
    letter-spacing: 0.12em;
    color: var(--white);
    margin: 0;
  }
  .holder__role {
    font-family: "Michroma", sans-serif;
    font-size: 10px;
    letter-spacing: 0.22em;
    color: var(--cyan);
    margin: 4px 0 0;
  }
  .contact {
    position: absolute;
    left: 40px; top: 106px;
    font-family: "Roboto", sans-serif;
    font-size: 13px;
    color: var(--white);
    list-style: none;
    margin: 0; padding: 0;
  }
  .contact li { display: flex; align-items: center; gap: 8px; margin-bottom: 6px; }
  .contact svg { width: 12px; height: 12px; }
  .divider {
    position: absolute;
    left: 40px; right: 40px; top: 160px;
    height: 1px;
    background: rgba(244,245,251,0.45);
  }
  .address {
    position: absolute;
    right: 40px; bottom: 40px;
    text-align: right;
    font-family: "Roboto", sans-serif;
    font-size: 13px;
    line-height: 1.45;
    color: var(--white);
    margin: 0;
  }
  .wave-area {
    position: absolute;
    left: 0; top: 176px;
    width: 330px; height: 190px;
    background:
      radial-gradient(ellipse 70% 80% at 20% 100%, rgba(82,88,171,0.55) 0%, rgba(82,88,171,0) 70%),
      radial-gradient(ellipse 60% 50% at 0% 20%, rgba(11,180,238,0.25) 0%, rgba(11,180,238,0) 70%);
  }
</style>
</head>
<body>
<main class="canvas">

  <section class="card card--back" aria-label="Card back">
    <div class="wordmark">
      <div>HALDANE</div>
      <div class="wordmark__sub">SUBSEA SERVICES</div>
    </div>
  </section>

  <section class="card card--front" aria-label="Card front">
    <div class="wave-area" role="img" aria-label="Decorative flowing wave swooshes in cyan and periwinkle"></div>

    <div class="holder">
      <p class="holder__name">OWEN MARSH</p>
      <p class="holder__role">DIRECTOR</p>
    </div>

    <ul class="contact">
      <li>
        <svg viewBox="0 0 12 12" aria-hidden="true"><path d="M2 1h3l1 3-2 1a7 7 0 0 0 3 3l1-2 3 1v3c-6 1-10-3-9-9z" fill="var(--cyan)"/></svg>
        0261-7730-4815
      </li>
      <li>
        <svg viewBox="0 0 12 12" aria-hidden="true"><rect x="3" y="0.5" width="6" height="11" rx="1.2" fill="none" stroke="var(--cyan)" stroke-width="1.2"/></svg>
        0261-7730-4815
      </li>
    </ul>

    <div class="divider"></div>

    <div class="wordmark">
      <div>HALDANE</div>
      <div class="wordmark__sub">SUBSEA SERVICES</div>
    </div>

    <p class="address">27 Tidewater Pde<br>Seaholm VIC 3018</p>
  </section>

</main>
</body>
</html>
```